■依頼の目的/概要
池袋、渋谷にある猫カフェ「PuRLi」の
店頭看板用ポスターを作成して頂きたいです。

■PuRLi概要

PuRLiは渋谷・池袋にある猫カフェです。
http://cafepurli.jp/

-最近、猫と遊んだことありますか?-

猫をなでたり、一緒に遊んだり、
PuRLiは猫たちとの癒しの時間をゆったりと過ごせる空間を提供しております。

池袋店は、木のぬくもりが感じられるこだわりの内装と明るい店内。
元気一杯の猫ちゃんたちと触れ合えるお店です。

新たにオープンした渋谷店は
都会の喧騒を忘れさせる落ち着いた店内が特長。
店舗が8・9階なので渋谷が一望できる最高の見晴らし&落ち着いた空間で
猫たちと触れ合うことができます。

内装だけでなく、においなどの衛生面に配慮し、
従来の猫カフェのイメージを払拭すべく、おしゃれで誰でも立ち寄れる猫カフェを目指しています。

おしゃれな猫カフェとして
様々なメディアにも取り上げられております。

プレスリリース
http://newswirez.jp/main/html/rd/p/000000001.000014659.html

まるでバーのような猫カフェ
http://news.tabiroute.jp/news/2015/07/23/340/

おしゃれ過ぎる大人の猫カフェ
http://beauty.kumoraku.co.jp/buzz/articles/216875

POKOニュース
http://news.poko.me/issue/odekake/ae588d362140

もっふもふに勝る癒しなし?
http://hu-t.me/article/173012970747529840

ヨリドリ!
http://www.yori-dori.com/content/11601/

聞いてPIKO
http://kiite.piko.ne.jp/watch/entry/675b5c9870a0e51eccd6b58452015943/

■依頼詳細

・サイズ
B1:横幅(mm)728、高さ(mm)1030

記載事項
・PuRLiロゴ
・キャッチコピー(仮)
「最近、猫と遊んだことありますか?」
・当ビル8階
・OPEN 10:00~22:00(最終入店21:30)
・10分 200円(税別)

・ドリンクバー ¥350(税別)
・漫画 雑誌
・Wi-Fi
・電源/コンセント

・中学生以上入場可能
・電話番号:03-5812-7740
・English OK
・中文 OK
・URL:cafepurli.jp/

※言い回しや表記は意味合いが変わらないようであれば
日本語・英語表記の変更OKです。

★ロゴデータを添付しておりますのでご使用下さい。
猫の参考、素材写真は下記URLよりダウンロード可能です。
http://11.sendraku.nu/h7b911505013ee928d2f67a1ce7fb821d-0925

■納品ファイル
・高解像度JPG (.jpg)
・イラストレーター形式 (.ai)

■重視する点

街を歩いているときに目を引く、PuRLiへ行ってみたいと思わせる、
ついつい足をとめて見てしまうようなデザインを求めています。

渋谷・池袋の両店舗前に設置する店頭ポスター(看板)として使用いたします。
デザインの決定後、記載情報などの変更をお願いをいたします。

写真とキャッチの魅せ方
文字情報のメリハリ
情報の伝わりやすさ
目を惹く素晴らしいデザインでした。

この度は猫カフェの店頭ポスターへご提案頂き、ありがとうござました。
予想を遥かに越えるご提案数に加え、レベルの高いデザインが多く、
選考に困難を極めました。
沢山のご提案感謝いたします。
次の機会もぜひよろしくお願いいたします。

```html
<!DOCTYPE html>
<html lang="ja">
<head>
<meta charset="utf-8">
<title>猫cafe PuRLi 店頭ポスター</title>
<link rel="stylesheet" href="https://fonts.googleapis.com/css2?family=Noto+Sans+JP:wght@400;500;700;900&display=swap">
<style>
  :root {
    --charcoal: #3b3b3d;
    --charcoal-deep: #2e2e30;
    --gold: #c8a75a;
    --mustard: #e3ad1f;
    --white: #ffffff;
    --ink: #333333;
    --panel: rgba(255, 255, 255, 0.88);
    --alert: #c0392b;
    --window: #eef1f3;
    --cushion: #cdbfa9;
    --brick: #5a4338;
    --wood: #8a6a52;
    --tabby: #8d8780;
  }
  * { box-sizing: border-box; margin: 0; padding: 0; }
  html, body { width: 848px; height: 1200px; overflow: hidden; background: var(--white); }
  body { font-family: "Noto Sans JP", sans-serif; color: var(--ink); }

  .poster { position: relative; width: 848px; height: 1200px; overflow: hidden; }

  .masthead {
    position: absolute; inset: 0 0 auto 0; height: 284px;
    background: var(--charcoal);
    text-align: center;
  }
  .masthead__tagline {
    position: absolute; top: 36px; left: 0; right: 0; padding-left: 150px;
    color: var(--gold); font-size: 18px; font-weight: 500; letter-spacing: 0.12em;
  }
  .brand {
    position: absolute; top: 76px; left: 192px;
    display: flex; align-items: center; gap: 70px;
  }
  .brand__mark {
    width: 140px; height: 140px; border-radius: 50%;
    background: var(--white);
  }
  .brand__name {
    color: var(--white); font-weight: 700; line-height: 1;
    display: flex; flex-direction: column; align-items: flex-start;
  }
  .brand__sub { font-size: 36px; letter-spacing: 0.06em; padding-left: 6px; }
  .brand__main { font-size: 80px; letter-spacing: 0.02em; margin-top: 6px; }
  .masthead__url {
    position: absolute; top: 230px; left: 0; right: 0; padding-left: 150px;
    color: var(--gold); font-size: 24px; font-weight: 500; letter-spacing: 0.06em;
  }

  .hero {
    position: absolute; top: 284px; left: 0; width: 848px; height: 848px;
    background:
      radial-gradient(ellipse 30% 22% at 54% 72%, rgba(120,112,104,0.95) 0%, rgba(141,135,128,0.6) 45%, rgba(141,135,128,0) 100%),
      radial-gradient(ellipse 16% 14% at 74% 52%, rgba(125,118,110,0.85) 0%, rgba(125,118,110,0) 100%),
      radial-gradient(ellipse 26% 22% at 10% 40%, rgba(205,191,169,0.95) 0%, rgba(205,191,169,0) 100%),
      radial-gradient(ellipse 24% 20% at 4% 78%, rgba(190,176,158,0.9) 0%, rgba(190,176,158,0) 100%),
      linear-gradient(180deg, rgba(0,0,0,0) 0%, rgba(0,0,0,0) 80%, rgba(138,106,82,0.85) 90%, rgba(110,84,66,0.95) 100%),
      linear-gradient(90deg, #dfe2e3 0%, var(--window) 28%, #f2f3f2 50%, #cfc6bc 66%, var(--brick) 80%, #6e5445 90%, #3e2e26 100%);
  }
  .hero__catch {
    position: absolute; top: 18px; left: 380px;
    padding: 10px 18px;
    background: rgba(255,255,255,0.45);
    font-size: 41px; font-weight: 500; line-height: 2.2; color: var(--ink);
    letter-spacing: 0.06em;
  }

  .info {
    position: absolute; top: 996px; left: 22px; right: 22px;
    display: grid; grid-template-columns: repeat(4, 1fr); gap: 16px;
  }
  .info__card { display: flex; flex-direction: column; }
  .info__head {
    background: var(--charcoal-deep); color: var(--white);
    font-size: 18px; font-weight: 700; text-align: center; letter-spacing: 0.1em;
    padding: 6px 0; border-radius: 6px 6px 0 0;
  }
  .info__head small { font-size: 11px; font-weight: 500; letter-spacing: 0; }
  .info__body {
    background: var(--panel); height: 96px; padding: 8px 10px;
    border-radius: 0 0 6px 6px; text-align: center;
    font-size: 17px; font-weight: 700; line-height: 1.4;
  }
  .info__note { font-size: 12px; font-weight: 500; }
  .info__note--alert { color: var(--alert); }
  .info__big { font-size: 24px; font-weight: 900; }
  .services { list-style: none; text-align: left; font-size: 15px; font-weight: 500; padding-left: 14px; }
  .services li::before { content: "・"; }
  .phone { font-size: 21px; font-weight: 900; letter-spacing: 0.02em; margin-top: 6px; }
  .lang-tag {
    display: inline-block; margin-top: 10px; padding: 2px 12px;
    background: var(--mustard); color: var(--ink); font-size: 14px; font-weight: 700;
  }

  .floor-band {
    position: absolute; left: 0; right: 0; bottom: 0; height: 68px;
    background: var(--mustard); color: var(--white);
    display: flex; align-items: center; justify-content: center;
    font-size: 34px; font-weight: 700; letter-spacing: 0.12em;
  }
</style>
</head>
<body>
<main class="poster">
  <header class="masthead">
    <p class="masthead__tagline">猫と遊べる大人の癒し空間</p>
    <div class="brand">
      <span class="brand__mark" aria-hidden="true"></span>
      <p class="brand__name"><span class="brand__sub">猫 cafe</span><span class="brand__main">PuRLi</span></p>
    </div>
    <p class="masthead__url">cafepurli.jp/</p>
  </header>

  <section class="hero" role="img" aria-label="明るい窓辺の木の棚に立つ縞模様の子猫、左にクッション、右にレンガ壁の写真">
    <h1 class="hero__catch">最近、猫と<br>遊んだこと<br>ありますか？</h1>
  </section>

  <section class="info">
    <div class="info__card">
      <h2 class="info__head">OPEN</h2>
      <div class="info__body">
        <p class="info__big">10:00 ~ 22:00</p>
        <p class="info__note">(最終入店 21:30)</p>
        <p class="info__note info__note--alert">※中学生以上入場可能</p>
      </div>
    </div>
    <div class="info__card">
      <h2 class="info__head">料金 <small>(税別)</small></h2>
      <div class="info__body">
        <p><span class="info__big">10分 200円</span></p>
        <p style="margin-top:8px">ドリンクバー <span class="info__big" style="font-size:20px">350円</span></p>
      </div>
    </div>
    <div class="info__card">
      <h2 class="info__head">その他サービス</h2>
      <div class="info__body">
        <ul class="services">
          <li>漫画 雑誌</li>
          <li>Wi-Fi</li>
          <li>電源 / コンセント</li>
        </ul>
      </div>
    </div>
    <div class="info__card">
      <h2 class="info__head">お問い合わせ</h2>
      <div class="info__body">
        <p class="phone">03-5812-7740</p>
        <p class="lang-tag">English / 中文 OK</p>
      </div>
    </div>
  </section>

  <footer class="floor-band">当ビル８階へお越しくださいませ</footer>
</main>
</body>
</html>
```